Business Card Design Project

Same as the logo requirements.
Address of the store is:
Milo's Waypost, LLC
287B North Ferncliff Ave Suite 4
Marlow Falls, IN 46592
Gerald Pinkney, Owner

Reason: The design of the business cards should be the same as the main logo.

Reason: I approved the wrong design!

This is the link to the current logo design: http://files.pixelbazaar-example.net/img/720415/391826/391826_5092741_720415_image.jpg

Target Market(s)

Courthouse and downtown employees, including lawyers, judges, downtown office workers.

Industry/Entity Type

Store

Font styles to use
Serif

Requirements
Must have
• Milo's Waypost
A Convenience Store, and More, on Lindenfield Plaza!
Marlow Falls, IN 46592
Nice to have
• Colorful, Arrow sign

```html
<!DOCTYPE html>
<html lang="en">
<head>
<meta charset="utf-8">
<title>Milo's Waypost, LLC — Business Card</title>
<link rel="stylesheet" href="https://fonts.googleapis.com/css2?family=Cinzel:wght@400;700&display=swap">
<style>
  :root {
    --page-bg: #ecebe8;
    --card-blue: #a3bbe3;
    --card-white: #ffffff;
    --ink-navy: #2d4786;
    --card-shadow: rgba(40, 40, 50, 0.22);
  }
  * { box-sizing: border-box; margin: 0; padding: 0; }
  html, body {
    width: 1200px;
    height: 800px;
    overflow: hidden;
    background: var(--page-bg);
  }
  .canvas {
    width: 1200px;
    height: 800px;
    display: flex;
    align-items: center;
    justify-content: center;
  }
  .business-card {
    position: relative;
    width: 980px;
    height: 560px;
    display: flex;
    background: var(--card-white);
    box-shadow: 0 14px 40px var(--card-shadow);
    font-family: "Cinzel", "Times New Roman", serif;
    color: var(--ink-navy);
  }
  .brand-panel {
    width: 480px;
    height: 100%;
    background: var(--card-blue);
    display: flex;
    flex-direction: column;
    align-items: center;
    justify-content: center;
    gap: 26px;
  }
  .brand-dot {
    width: 58px;
    height: 58px;
    border-radius: 50%;
    background: var(--ink-navy);
  }
  .brand-name {
    font-size: 38px;
    font-weight: 400;
    letter-spacing: 0.5px;
    white-space: nowrap;
  }
  .contact-panel {
    flex: 1;
    padding: 58px 24px 0 40px;
  }
  .owner-name {
    font-size: 44px;
    font-weight: 400;
    line-height: 1;
    white-space: nowrap;
    margin-left: 18px;
  }
  .owner-role {
    font-size: 24px;
    font-weight: 700;
    margin-top: 4px;
  }
  .contact-list {
    list-style: none;
    margin-top: 70px;
    display: flex;
    flex-direction: column;
    gap: 22px;
  }
  .contact-item {
    display: flex;
    align-items: flex-start;
    gap: 20px;
    font-size: 19px;
    line-height: 1.3;
  }
  .contact-icon {
    width: 22px;
    height: 26px;
    flex: none;
    fill: var(--ink-navy);
    margin-top: -14px;
  }
  .contact-text {
    margin-top: 6px;
    white-space: nowrap;
  }
</style>
</head>
<body>
<main class="canvas">
  <article class="business-card">
    <section class="brand-panel">
      <span class="brand-dot" aria-hidden="true"></span>
      <h1 class="brand-name">Milo's Waypost, LLC</h1>
    </section>
    <section class="contact-panel">
      <h2 class="owner-name">Gerald Pinkney</h2>
      <p class="owner-role">Owner</p>
      <ul class="contact-list">
        <li class="contact-item">
          <svg class="contact-icon" viewBox="0 0 24 24" aria-label="Phone">
            <path d="M6.6 10.8c1.4 2.8 3.8 5.1 6.6 6.6l2.2-2.2c.3-.3.7-.4 1-.2 1.1.4 2.3.6 3.6.6.6 0 1 .4 1 1V20c0 .6-.4 1-1 1C10.6 21 3 13.4 3 4c0-.6.4-1 1-1h3.5c.6 0 1 .4 1 1 0 1.3.2 2.5.6 3.6.1.3 0 .7-.2 1L6.6 10.8z"/>
          </svg>
          <span class="contact-text">+1 (330) 5550 172</span>
        </li>
        <li class="contact-item">
          <svg class="contact-icon" viewBox="0 0 24 24" aria-label="Address">
            <path d="M12 2C8.1 2 5 5.1 5 9c0 5.2 7 13 7 13s7-7.8 7-13c0-3.9-3.1-7-7-7zm0 9.5a2.5 2.5 0 1 1 0-5 2.5 2.5 0 0 1 0 5z"/>
          </svg>
          <span class="contact-text">287B North Ferncliff Ave Suite 4<br>Marlow Falls, IN 46592</span>
        </li>
      </ul>
    </section>
  </article>
</main>
</body>
</html>
```